Plakat-Design für Musikwettbewerb-Veranstalter
Zielgruppe
Wir veranstalten Musikwettbewerbe an Schulen. Zielgruppe sind Schüler und ihre Eltern, männlich/weiblich 40/60, u25/ü25 ca. 50/50
Aufgabenstellung
Wir sind gespannt, gerne frei denken, Logo anbei, weitere Infos auf der Homepage www.klangfuchs-wettbewerb.de, Inhalte lt. altem Plakat (ebenfalls anbei)

```html
<!DOCTYPE html>
<html lang="de">
<head>
<meta charset="utf-8">
<title>Klangfuchs – Vorentscheid Lindorf</title>
<link href="https://fonts.googleapis.com/css2?family=Roboto+Slab:wght@700;900&display=swap" rel="stylesheet">
<style>
  :root {
    --stage: #c9c9c9;
    --paper-top: #ffffff;
    --paper-mid: #e6d6ee;
    --paper-low: #b58bd0;
    --red: #d31f2a;
    --green: #3ee23a;
    --slate: #3f5568;
    --black: #0d0d0d;
    --yellow: #fdc43a;
    --white: #ffffff;
    --ink: #111111;
    --alert: #e3131f;
  }
  html, body {
    margin: 0;
    width: 1200px;
    height: 675px;
    overflow: hidden;
    background: var(--stage);
  }
  .poster {
    position: absolute;
    left: 353px;
    top: 12px;
    width: 494px;
    height: 650px;
    font-family: "Roboto Slab", Georgia, serif;
  }
  .poster svg { display: block; width: 494px; height: 650px; }
  .poster text { font-family: "Roboto Slab", Georgia, serif; font-weight: 700; }
  .headline { font-weight: 900; }
</style>
</head>
<body>
<main class="poster">
  <svg viewBox="0 0 494 650" xmlns="http://www.w3.org/2000/svg">
    <defs>
      <linearGradient id="paper" x1="0" y1="0" x2="0" y2="1">
        <stop offset="0" stop-color="var(--paper-top)"/>
        <stop offset="0.35" stop-color="var(--paper-mid)"/>
        <stop offset="0.8" stop-color="var(--paper-low)"/>
      </linearGradient>
      <linearGradient id="splash" x1="0" y1="0" x2="1" y2="0">
        <stop offset="0" stop-color="#ff2a9a"/>
        <stop offset="0.35" stop-color="#f6a21c"/>
        <stop offset="0.65" stop-color="#8cd63a"/>
        <stop offset="1" stop-color="#f3ea2e"/>
      </linearGradient>
    </defs>

    <rect class="paper" width="494" height="650" fill="url(#paper)"/>

    <!-- brand mark -->
    <g class="brand">
      <ellipse role="img" aria-label="Farbige Illustration mit Musikinstrumenten: Gitarren, Tuba, Schlagzeug und Keyboard" cx="190" cy="84" rx="150" ry="62" fill="url(#splash)" opacity="0.85"/>
      <text x="185" y="100" text-anchor="middle" font-size="48" fill="var(--white)" class="headline" transform="rotate(-6 185 100)">Klangfuchs</text>
    </g>

    <!-- event banners -->
    <polygon class="band-red" points="46,156 455,138 469,191 37,208" fill="var(--red)"/>
    <text x="252" y="192" text-anchor="middle" font-size="44" fill="var(--white)" transform="rotate(-2 252 192)">VORENTSCHEID</text>

    <polygon class="band-green" points="227,209 455,205 457,263 211,268" fill="var(--green)"/>
    <text x="338" y="256" text-anchor="middle" font-size="52" fill="var(--white)">Lindorf</text>

    <polygon class="band-date" points="128,287 437,281 487,356 471,384 87,391" fill="var(--slate)"/>
    <text x="298" y="334" text-anchor="middle" font-size="47" fill="var(--white)">11.07.2017</text>
    <text x="287" y="384" text-anchor="middle" font-size="50" fill="var(--white)">Ab 19:00 Uhr</text>

    <polygon class="band-schools" points="0,403 343,400 368,475 0,497" fill="var(--black)"/>
    <g fill="var(--white)" font-size="19" text-anchor="middle" transform="rotate(-2 180 455)">
      <text x="180" y="432">Birkenhof-Schule</text>
      <text x="180" y="457">Berufliche Schule Lindorf</text>
      <text x="180" y="482">Gemeinschaftsschule Lindorf</text>
    </g>

    <!-- info block -->
    <polygon class="band-info" points="0,506 494,478 494,614 0,614" fill="var(--yellow)"/>
    <g fill="var(--ink)" font-size="15" text-anchor="middle">
      <text x="121" y="524">Mensa der</text>
      <text x="121" y="539">Birkenhof-Schule</text>
      <text x="121" y="554">Birkenhofweg 5</text>
      <text x="121" y="570">25000 Lindorf</text>
    </g>
    <g fill="var(--ink)" font-size="24">
      <text x="240" y="519">Einlass: 18:30 Uhr</text>
      <text x="240" y="546">Beginn: 19:00 Uhr</text>
      <text x="242" y="573">Vvk: 3 € | Ak: 4 €</text>
    </g>
    <text x="247" y="594" text-anchor="middle" font-size="12.5" fill="var(--alert)">Bewerbung für Künstler unter www.klangfuchs-wettbewerb.de/bewerbung</text>
    <text x="247" y="609" text-anchor="middle" font-size="12" fill="var(--ink)">www.klangfuchs-wettbewerb.de | www.fuchsnetz.de/klangfuchs</text>

    <!-- partners -->
    <rect y="613" width="494" height="2" fill="var(--black)"/>
    <rect y="615" width="494" height="35" fill="var(--white)"/>
    <g font-size="12" fill="var(--ink)">
      <text x="60" y="637" fill="var(--red)">Sparfeld</text>
      <text x="128" y="637" fill="var(--slate)">Hallklang</text>
      <text x="200" y="637" fill="var(--red)">Notenrecht</text>
      <text x="284" y="637">Tonwerk</text>
      <text x="355" y="637" fill="var(--slate)">Land Nordmark</text>
    </g>
  </svg>
</main>
</body>
</html>
```